Linked In Profile Banner Needed

I am in need of a Linked In Banner photo for my profile. The dimensions are 1584 x 396 pixels and the bottom left is where Linked In places my photo over so be aware of that. I attached an example for your reference.

I have also attached my logo and business card so you can keep the same color & style conistant.

Also add the following text:

"Preserve capital with a tax advantaged lease for equipment, vehicles, software and more! $5,000 - $50m"

You can also look at our website here:
www.HarlowfieldFundingCo.com

```html
<!DOCTYPE html>
<html lang="en">
<head>
<meta charset="utf-8">
<title>Harlowfield Funding Co. – Profile Banner</title>
<link rel="stylesheet" href="https://fonts.googleapis.com/css2?family=Bebas+Neue&family=Roboto:wght@300;400&display=swap">
<style>
  :root {
    --navy: #272641;
    --navy-soft: #2d3355;
    --navy-glow: #2f3d5f;
    --white: #ffffff;
    --accent: #4ec5ea;
    --rule: #6f84b8;
  }
  html, body {
    margin: 0;
    padding: 0;
    width: 1200px;
    height: 300px;
    overflow: hidden;
    background: var(--navy);
  }
  .banner {
    position: relative;
    width: 1200px;
    height: 300px;
    background: var(--navy);
    overflow: hidden;
    font-family: "Roboto", Arial, sans-serif;
    color: var(--white);
  }
  .backdrop {
    position: absolute;
    left: 0;
    top: 0;
    width: 290px;
    height: 300px;
    background: linear-gradient(160deg, var(--navy-glow) 0%, var(--navy-soft) 55%, var(--navy) 100%);
  }
  .brand {
    position: absolute;
    left: 56px;
    top: 56px;
    display: flex;
    align-items: center;
    gap: 10px;
  }
  .brand-mark {
    width: 18px;
    height: 18px;
    background: var(--accent);
  }
  .brand-name {
    font-family: "Roboto", Arial, sans-serif;
    font-weight: 300;
    font-size: 20px;
    letter-spacing: 1.5px;
    color: var(--white);
    text-transform: uppercase;
    white-space: nowrap;
  }
  .headline {
    position: absolute;
    left: 389px;
    top: 30px;
    margin: 0;
    font-family: "Bebas Neue", "Oswald", sans-serif;
    font-weight: 400;
    font-size: 35px;
    line-height: 33px;
    letter-spacing: 1.6px;
    color: var(--white);
    white-space: nowrap;
  }
  .headline .range { color: var(--accent); }
  .benefits {
    position: absolute;
    margin: 0;
    padding: 0;
    list-style: none;
  }
  .benefits-left { left: 386px; top: 116px; }
  .benefits-right { left: 747px; top: 113px; }
  .benefit {
    position: relative;
    padding-left: 16px;
    height: 57px;
  }
  .benefit::before {
    content: "";
    position: absolute;
    left: 0;
    top: 9px;
    width: 4px;
    height: 4px;
    border-radius: 50%;
    background: var(--white);
  }
  .benefit-title {
    display: block;
    font-size: 13.5px;
    line-height: 16px;
    letter-spacing: 0.6px;
    color: var(--white);
  }
  .benefit-text {
    display: block;
    font-size: 11.3px;
    line-height: 13.5px;
    letter-spacing: 0.5px;
    color: var(--accent);
  }
  .site {
    position: absolute;
    right: 42px;
    top: 247px;
    padding-top: 7px;
    border-top: 1px solid var(--rule);
    font-size: 14px;
    letter-spacing: 0.5px;
    color: var(--white);
  }
</style>
</head>
<body>
<main class="banner">
  <div class="backdrop" role="img" aria-label="Soft navy decorative backdrop"></div>

  <div class="brand">
    <span class="brand-mark"></span>
    <span class="brand-name">Harlowfield Funding Co.</span>
  </div>

  <h1 class="headline">
    Preserve capital with a tax advantaged lease<br>
    for equipment, vehicles, software and more! <span class="range">$5,000 – $50M</span>
  </h1>

  <ul class="benefits benefits-left">
    <li class="benefit">
      <span class="benefit-title">Preserve Cash Flow</span>
      <span class="benefit-text">Leasing allows you to retain cash for other operational<br>needs or investments</span>
    </li>
    <li class="benefit">
      <span class="benefit-title">Easier Financing Approval</span>
      <span class="benefit-text">Leasing often has less stringent credit requirements<br>compared to traditional loans.</span>
    </li>
    <li class="benefit">
      <span class="benefit-title">Improve Financial Ratios</span>
      <span class="benefit-text">Leasing keeps liabilities off your balance sheet,<br>improving debt-to-equity and other financial ratios.</span>
    </li>
  </ul>

  <ul class="benefits benefits-right">
    <li class="benefit">
      <span class="benefit-title">Tax Advantages</span>
      <span class="benefit-text">Lease payments can be tax deductible as an<br>operating expense, reducing your taxable income.</span>
    </li>
    <li class="benefit">
      <span class="benefit-title">Conserve Borrowing Power</span>
      <span class="benefit-text">Leasing doesn't tie up credit, leaving room for<br>other financing opportunities.</span>
    </li>
  </ul>

  <div class="site">www.HarlowfieldFundingCo.com</div>
</main>
</body>
</html>
```